WordPress Site Design and Code for Technology Consulting Startup

We need a WordPress design and code to a new site on Tallow Bay. We have the logo and colors ready. The site will be a brochure site with a CONTACT page that contains a form that the prospective client fills out. The other pages would be ABOUT / SERVICES (3 option drop-down) / SUPPORT. The site should be appropriate for an IT Consulting / IT Managed Services / IT Project Management services in the Chicago area.

Across small, medium, large businesses.

Technology, network infrastructure, IT.

Coded - Design and coding required

5+ page

• I prefer mid-modern / simple / art deco / minimalist.

```html
<!DOCTYPE html>
<html lang="en">
<head>
<meta charset="utf-8">
<title>Norvane — Header Variants</title>
<link href="https://fonts.googleapis.com/css2?family=Montserrat:wght@400;500;600;700&display=swap" rel="stylesheet">
<style>
  :root {
    --ink: #07090c;
    --teal: #1e95ad;
    --orange: #f26f21;
    --white: #ffffff;
    --paper: #ffffff;
  }
  * { box-sizing: border-box; margin: 0; padding: 0; }
  html, body { width: 1200px; height: 577px; overflow: hidden; background: var(--paper); }
  body { position: relative; font-family: "Montserrat", sans-serif; }

  .header {
    position: absolute; left: 72px; width: 1054px; height: 84px;
    background: var(--bg); color: var(--fg);
    box-shadow: 0 12px 10px -6px rgba(0,0,0,0.35);
  }
  .header--dark  { top: 93px;  --bg: var(--ink);  --fg: var(--white); --brand: var(--teal);  --rule: var(--teal); }
  .header--light { top: 243px; --bg: var(--white); --fg: var(--ink); --brand: var(--teal); --rule: var(--teal); }
  .header--teal  { top: 393px; --bg: var(--teal); --fg: var(--white); --brand: var(--white); --rule: rgba(255,255,255,0.75); }

  .brand {
    position: absolute; left: 0; top: 0; width: 155px; height: 84px;
    display: flex; align-items: center; justify-content: center; gap: 7px;
    color: var(--brand); font-weight: 700; font-size: 19px; letter-spacing: 1px; text-transform: uppercase;
  }
  .brand__mark { width: 9px; height: 9px; background: var(--orange); }

  .topbar {
    position: absolute; left: 175px; top: 0; width: 761px; height: 27px;
    border-left: 1px solid var(--rule); border-right: 1px solid var(--rule); border-bottom: 1px solid var(--rule);
    font-size: 12px; display: flex; align-items: center;
  }
  .topbar__item { position: absolute; display: flex; align-items: center; gap: 8px; white-space: nowrap; }
  .topbar__item--email { left: 14px; }
  .topbar__item--address { left: 214px; }
  .topbar__links { position: absolute; right: 14px; }
  .icon-orange { fill: var(--orange); }

  .social { position: absolute; left: 951px; top: 6px; display: flex; gap: 11px; }
  .social__dot { width: 13px; height: 13px; border-radius: 50%; background: var(--fg); }

  .nav { position: absolute; left: 190px; top: 44px; display: flex; gap: 15px; font-size: 16.5px; font-weight: 500; }
  .nav__item { display: flex; align-items: center; gap: 4px; }
  .nav__chevron { width: 10px; height: 7px; fill: none; stroke: var(--fg); stroke-width: 2.4; }

  .call { position: absolute; left: 730px; top: 40px; display: flex; align-items: center; gap: 15px; }
  .call__badge {
    width: 29px; height: 29px; border-radius: 50%;
    display: flex; align-items: center; justify-content: center;
    background: var(--badge); 
  }
  .header--dark  .call__badge { --badge: linear-gradient(135deg, var(--teal), var(--orange)); --phone: var(--white); }
  .header--light .call__badge { --badge: linear-gradient(135deg, var(--ink) 55%, var(--orange)); --phone: var(--white); }
  .header--teal  .call__badge { --badge: var(--white); --phone: var(--ink); }
  .call__badge svg { width: 14px; height: 14px; fill: var(--phone); }
  .call__label { font-size: 10.5px; line-height: 1.1; }
  .call__number { font-size: 14.5px; font-weight: 700; line-height: 1.2; }

  .quote {
    position: absolute; left: 938px; top: 41px; width: 109px; height: 28px;
    display: flex; align-items: center; justify-content: center;
    font-size: 13px; font-weight: 700; color: var(--fg);
    border: 1.5px solid var(--orange); border-left-color: var(--teal); border-top-color: var(--teal);
  }
  .header--teal .quote { border-color: var(--orange); }
</style>
</head>
<body>

<svg width="0" height="0" style="position:absolute">
  <defs>
    <symbol id="i-mail" viewBox="0 0 16 12"><path d="M0 0h16v12H0z M0 1l8 5 8-5" /><path d="M1 1.5l7 4.5 7-4.5" fill="none" stroke="#fff" stroke-width="1.4"/></symbol>
    <symbol id="i-pin" viewBox="0 0 12 16"><path d="M6 0a6 6 0 0 0-6 6c0 4.5 6 10 6 10s6-5.5 6-10a6 6 0 0 0-6-6zm0 8.5a2.5 2.5 0 1 1 0-5 2.5 2.5 0 0 1 0 5z"/></symbol>
    <symbol id="i-phone" viewBox="0 0 24 24"><path d="M6.6 10.8a15.1 15.1 0 0 0 6.6 6.6l2.2-2.2c.3-.3.7-.4 1-.2 1.1.4 2.3.6 3.6.6.6 0 1 .4 1 1V20c0 .6-.4 1-1 1A17 17 0 0 1 3 4c0-.6.4-1 1-1h3.5c.6 0 1 .4 1 1 0 1.3.2 2.5.6 3.6.1.3 0 .7-.2 1z"/></symbol>
  </defs>
</svg>

<header class="header header--dark">
  <div class="brand"><span class="brand__mark"></span>Norvane</div>
  <div class="topbar">
    <span class="topbar__item topbar__item--email"><svg class="icon-orange" width="14" height="11"><use href="#i-mail"/></svg>needhelp@norvane.com</span>
    <span class="topbar__item topbar__item--address"><svg class="icon-orange" width="10" height="14"><use href="#i-pin"/></svg>42 LINDEN AVE. Chicago</span>
    <span class="topbar__links">Help / Support / Contact</span>
  </div>
  <div class="social" aria-label="Social links"><span class="social__dot"></span><span class="social__dot"></span><span class="social__dot"></span><span class="social__dot"></span></div>
  <nav class="nav">
    <span class="nav__item">Home</span><span class="nav__item">About</span>
    <span class="nav__item">Services<svg class="nav__chevron" viewBox="0 0 10 7"><path d="M1 1l4 4 4-4"/></svg></span>
    <span class="nav__item">Contact</span>
  </nav>
  <div class="call">
    <span class="call__badge"><svg><use href="#i-phone"/></svg></span>
    <div><div class="call__label">Call Anytime</div><div class="call__number">+1 555 (010) 0420</div></div>
  </div>
  <span class="quote">Get a quote</span>
</header>

<header class="header header--light">
  <div class="brand"><span class="brand__mark"></span>Norvane</div>
  <div class="topbar">
    <span class="topbar__item topbar__item--email"><svg class="icon-orange" width="14" height="11"><use href="#i-mail"/></svg>needhelp@norvane.com</span>
    <span class="topbar__item topbar__item--address"><svg class="icon-orange" width="10" height="14"><use href="#i-pin"/></svg>42 LINDEN AVE. Chicago</span>
    <span class="topbar__links">Help / Support / Contact</span>
  </div>
  <div class="social" aria-label="Social links"><span class="social__dot"></span><span class="social__dot"></span><span class="social__dot"></span><span class="social__dot"></span></div>
  <nav class="nav">
    <span class="nav__item">Home</span><span class="nav__item">About</span>
    <span class="nav__item">Services<svg class="nav__chevron" viewBox="0 0 10 7"><path d="M1 1l4 4 4-4"/></svg></span>
    <span class="nav__item">Contact</span>
  </nav>
  <div class="call">
    <span class="call__badge"><svg><use href="#i-phone"/></svg></span>
    <div><div class="call__label">Call Anytime</div><div class="call__number">+1 555 (010) 0420</div></div>
  </div>
  <span class="quote">Get a quote</span>
</header>

<header class="header header--teal">
  <div class="brand"><span class="brand__mark"></span>Norvane</div>
  <div class="topbar">
    <span class="topbar__item topbar__item--email"><svg class="icon-orange" width="14" height="11"><use href="#i-mail"/></svg>needhelp@norvane.com</span>
    <span class="topbar__item topbar__item--address"><svg class="icon-orange" width="10" height="14"><use href="#i-pin"/></svg>42 LINDEN AVE. Chicago</span>
    <span class="topbar__links">Help / Support / Contact</span>
  </div>
  <div class="social" aria-label="Social links"><span class="social__dot"></span><span class="social__dot"></span><span class="social__dot"></span><span class="social__dot"></span></div>
  <nav class="nav">
    <span class="nav__item">Home</span><span class="nav__item">About</span>
    <span class="nav__item">Services<svg class="nav__chevron" viewBox="0 0 10 7"><path d="M1 1l4 4 4-4"/></svg></span>
    <span class="nav__item">Contact</span>
  </nav>
  <div class="call">
    <span class="call__badge"><svg><use href="#i-phone"/></svg></span>
    <div><div class="call__label">Call Anytime</div><div class="call__number">+1 555 (010) 0420</div></div>
  </div>
  <span class="quote">Get a quote</span>
</header>

</body>
</html>
```